WHERE RIVERS LEARN TO SING

Where Rivers Learn To Sing is the title of my book. The book is written to specifically address a major issue the world over which is the ability of think. Educational system in many parts of the world trains us to DO as supposed to Create. In the new world order, doing will always be inferior to thinking. The book is packed with methodologies and case studies. I need a unique design for the book.
Visual of the human brain as part of the creative element / rendition
Since the book is about creative thinking and innovation, I need a creative masterpiece that will be appealing to the eye on the shelf with a strong connection of curiosity & engagement. I personally am of the opinion that visual of the brain is quite off putting
AUTHOR: TUNDE OKORAFOR
PRINTED BY: MERIDIAN LEAF BOOKS
BOOK SIZE: A5

Target Market(s)

Middle to Senior Level Managers in the Private Sector, Fresh Graduates, Entrepreneurs & SME Owners, Government

Font styles to use
Serif

Colors

Designer to choose colors to be used in the design.

Requirements
Must have
• On the front cover, in addition to the title, it should also have the pay off ''Discover & Discover & Unleash The Power Of Your Creative Mind
• Simple back cover design that allows for authors note etc to be very legible
• another must have is space for authors picture
• Front cover Star Burst (WARNING: this book will be difficult to lend)
Should not have
• Visual of the human brain as part of the creative element / rendition

```html
<!DOCTYPE html>
<html lang="en">
<head>
<meta charset="utf-8">
<title>Where Rivers Learn To Sing — Book Cover</title>
<link rel="stylesheet" href="https://fonts.googleapis.com/css2?family=Cinzel:wght@400;500;700&family=Marcellus&family=Source+Sans+3:wght@400;700&display=swap">
<style>
  :root {
    --back-bg: #141414;
    --back-bg-top: #2c2c2c;
    --spine-bg: #0e0e0e;
    --olive: #7b7a1c;
    --title-light: #c9c9c9;
    --title-dark: #151515;
    --body-text: #e8e8e8;
    --photo-slot: #bdbdbd;
    --front-bg: #f4f4f4;
    --tagline: #2b2b2b;
    --author-front: #ffffff;
    --burst: #7b7a1c;
    --burst-text: #ffffff;
  }
  * { box-sizing: border-box; margin: 0; padding: 0; }
  html, body { width: 1200px; height: 818px; overflow: hidden; background: #ffffff; }
  .cover {
    position: relative;
    width: 1200px;
    height: 818px;
    overflow: hidden;
    font-family: "Marcellus", Georgia, serif;
  }

  /* Shared title */
  .title { position: absolute; left: 0; top: 0; height: 200px; font-family: "Cinzel", Georgia, serif; font-weight: 500; }
  .title-line1, .title-line2 { position: absolute; left: 0; width: 100%; text-align: center; line-height: 1; white-space: nowrap; }
  .title-line1 { top: 38px; font-size: 41px; letter-spacing: 0.5px; }
  .title-line2 { top: 94px; font-size: 104px; color: var(--olive); }

  /* Back cover */
  .back {
    position: absolute; left: 0; top: 0;
    width: 558px; height: 818px;
    background: radial-gradient(ellipse at 50% 0%, var(--back-bg-top) 0%, var(--back-bg) 60%);
  }
  .back .title { width: 558px; }
  .back .title-line1 { color: var(--title-light); }

  .back-blurb {
    position: absolute; left: 44px; top: 210px; width: 490px;
    font-size: 13px; line-height: 16.6px; color: var(--body-text); text-align: center;
  }
  .author-photo-slot {
    position: absolute; left: 44px; top: 380px; width: 182px; height: 209px;
    background: var(--photo-slot);
  }
  .author-note {
    position: absolute; left: 244px; top: 378px; width: 292px;
    font-size: 13px; line-height: 16.6px; color: var(--body-text); text-align: left;
  }
  .printer {
    position: absolute; left: 0; width: 558px; top: 774px; text-align: center;
    font-family: "Source Sans 3", Arial, sans-serif; font-size: 11.5px; color: var(--body-text);
    letter-spacing: 0.2px;
  }

  /* Spine */
  .spine {
    position: absolute; left: 558px; top: 0; width: 65px; height: 818px;
    background: var(--spine-bg);
  }
  .spine-title, .spine-author {
    position: absolute; left: 0; width: 65px;
    writing-mode: vertical-rl;
    font-family: "Cinzel", Georgia, serif;
    display: flex; align-items: center;
    white-space: nowrap;
  }
  .spine-title { top: 46px; color: #ffffff; font-size: 22px; letter-spacing: 0.5px; }
  .spine-author { top: 538px; color: var(--olive); font-size: 23px; font-weight: 700; letter-spacing: 1px; }

  /* Front cover */
  .front {
    position: absolute; left: 623px; top: 0; width: 577px; height: 818px;
    background: linear-gradient(160deg, #e4e4e4 0%, var(--front-bg) 35%, #ffffff 70%);
  }
  .front-glow {
    position: absolute; left: 230px; top: 180px; width: 520px; height: 700px;
    border-radius: 50%;
    background: #fdfbef;
  }
  .front .title { width: 577px; }
  .front .title-line1 { color: var(--title-dark); }

  .cover-art {
    position: absolute; left: 83px; top: 198px; width: 448px; height: 620px;
    border-radius: 200px 220px 0 0;
    background:
      radial-gradient(circle at 30% 15%, rgba(88,160,60,0.95) 0%, rgba(88,160,60,0) 35%),
      radial-gradient(circle at 70% 18%, rgba(226,140,40,0.95) 0%, rgba(226,140,40,0) 38%),
      radial-gradient(circle at 35% 55%, rgba(220,120,220,0.85) 0%, rgba(220,120,220,0) 40%),
      radial-gradient(circle at 75% 60%, rgba(245,220,80,0.9) 0%, rgba(245,220,80,0) 40%),
      radial-gradient(circle at 70% 95%, rgba(200,50,40,0.95) 0%, rgba(200,50,40,0) 45%),
      radial-gradient(circle at 20% 90%, rgba(40,110,80,0.9) 0%, rgba(40,110,80,0) 40%),
      linear-gradient(180deg, #9cc4d6 0%, #d7a9d8 50%, #c7553a 100%);
  }
  .tagline {
    position: absolute; left: 189px; top: 482px; width: 240px; text-align: center;
    font-family: "Source Sans 3", Arial, sans-serif; font-weight: 700;
    font-size: 20px; line-height: 29px; color: var(--tagline); letter-spacing: 0.3px;
  }
  .front-author {
    position: absolute; left: 0; width: 664px; top: 748px; text-align: center;
    font-family: "Cinzel", Georgia, serif; font-weight: 700;
    font-size: 38px; line-height: 1.2; color: var(--author-front); letter-spacing: 0.5px;
    white-space: nowrap;
  }

  /* Starburst */
  .starburst {
    position: absolute; left: 448px; top: 196px; width: 124px; height: 124px;
    transform: rotate(-8deg);
  }
  .starburst svg { position: absolute; left: 0; top: 0; width: 124px; height: 124px; }
  .starburst-text {
    position: absolute; left: 22px; top: 30px; width: 80px; height: 64px;
    display: flex; align-items: center; justify-content: center; text-align: center;
    font-family: "Source Sans 3", Arial, sans-serif; font-weight: 700;
    font-size: 10.5px; line-height: 12px; color: var(--burst-text);
  }
</style>
</head>
<body>
<div class="cover">

  <section class="back">
    <h2 class="title">
      <span class="title-line1">WHERE RIVERS LEARN</span>
      <span class="title-line2">TO SING</span>
    </h2>
    <p class="back-blurb">Lorem Ipsum is simply dummy text of the printing and typesetting industry. Lorem Ipsum has been the industry's standard dummy text ever since the 1500s, when an unknown printer took a galley of type and scrambled it to make a type specimen book. It has survived not only five centuries, but also the leap into electronic typesetting, remaining essentially unchanged. It was popularised in the 1960s with the release of Brightline sheets containing Lorem Ipsum passages, and more recently with desktop publishing software like Folio Studio including versions of Lorem Ipsum.</p>
    <div class="author-photo-slot" role="img" aria-label="Space for the author's portrait"></div>
    <p class="author-note">Lorem Ipsum is simply dummy text of the printing and typesetting industry. Lorem Ipsum has been the industry's standard dummy text ever since the 1500s, when an unknown printer took a galley of type and scrambled it to make a type specimen book. It has survived not only five centuries, but also the leap into electronic typesetting, remaining essentially unchanged. It was popularised in the 1960s with the release of Brightline sheets containing Lorem Ipsum passages, and more recently with desktop publishing software like Folio Studio including versions of Lorem Ipsum.</p>
    <p class="printer">PRINTED BY: MERIDIAN LEAF BOOKS</p>
  </section>

  <section class="spine">
    <div class="spine-title">WHERE RIVERS LEARN TO SING</div>
    <div class="spine-author">TUNDE OKORAFOR</div>
  </section>

  <section class="front">
    <div class="front-glow"></div>
    <h1 class="title">
      <span class="title-line1">WHERE RIVERS LEARN</span>
      <span class="title-line2">TO SING</span>
    </h1>
    <div class="cover-art" role="img" aria-label="Double-exposure silhouette of a man in profile filled with trees, city towers and overlapping rainbow-coloured circles"></div>
    <p class="tagline">DISCOVER &amp; UNLEASH THE POWER OF YOUR CREATIVE MIND</p>
    <div class="starburst">
      <svg viewBox="0 0 124 124" aria-hidden="true">
        <polygon fill="var(--burst)" points="122,62 110.3,74.9 114,92 97.4,97.4 92,114 74.9,110.3 62,122 49.1,110.3 32,114 26.6,97.4 10,92 13.7,74.9 2,62 13.7,49.1 10,32 26.6,26.6 32,10 49.1,13.7 62,2 74.9,13.7 92,10 97.4,26.6 114,32 110.3,49.1"/>
      </svg>
      <p class="starburst-text">WARNING: this book will be difficult to lend</p>
    </div>
    <p class="front-author">TUNDE OKORAFOR</p>
  </section>

</div>
</body>
</html>
```